Miriam Delacourt

I need a business card for my health consulting business specializing in yoga and coaching. I like clean, crisp designs. I would like some of the colors from the attachment to be incorporate. For font, I like Trajan Pro and Helvectica Neue but would be open to other similar fonts. The attached photo doesn't need to be incorporated directly but could be used as some sort of decoration. I would also like to have the icon incorporated into the design - but not the type.

Industry/Entity Type

Business

Font styles to use
Serif
Sans Serif

```html
<!DOCTYPE html>
<html lang="en">
<head>
<meta charset="utf-8">
<title>Miriam Delacourt Wellness – Business Card</title>
<link rel="stylesheet" href="https://fonts.googleapis.com/css2?family=Source+Sans+3:wght@400;600&display=swap">
<style>
  :root {
    --backdrop: #111111;
    --card: #ffffff;
    --ink: #9a7b5f;
    --accent: #d6c9bc;
    --shadow: rgba(0, 0, 0, 0.55);
  }
  * { margin: 0; padding: 0; box-sizing: border-box; }
  html, body {
    width: 1200px;
    height: 900px;
    overflow: hidden;
    background: var(--backdrop);
  }
  .stage {
    position: relative;
    width: 1200px;
    height: 900px;
    font-family: "Source Sans 3", "Helvetica Neue", sans-serif;
    color: var(--ink);
  }
  .card {
    position: absolute;
    top: 271px;
    width: 457px;
    height: 281px;
    background: var(--card);
    border-radius: 14px;
    box-shadow: 3px 4px 6px var(--shadow);
  }
  .card--front { left: 137px; }
  .card--back { left: 626px; }

  /* Brand name with plain dot */
  .brand {
    display: flex;
    align-items: center;
    font-weight: 600;
    color: var(--ink);
    white-space: nowrap;
  }
  .brand__dot {
    flex: none;
    border-radius: 50%;
    background: var(--accent);
  }

  /* Front */
  .card--front .brand {
    position: absolute;
    left: 44px;
    top: 96px;
    width: 184px;
    height: 90px;
    flex-direction: column;
    justify-content: center;
    gap: 10px;
    font-size: 13.5px;
  }
  .card--front .brand__dot { width: 24px; height: 24px; }

  .contact {
    position: absolute;
    left: 262px;
    top: 98px;
  }
  .contact__name {
    font-weight: 600;
    font-size: 18.5px;
    line-height: 22px;
  }
  .contact__role {
    font-size: 13px;
    line-height: 16px;
  }
  .contact__details {
    margin-top: 17px;
    font-size: 13px;
    line-height: 16px;
  }

  /* Back */
  .card--back .brand {
    position: absolute;
    left: 0;
    right: 0;
    top: 112px;
    justify-content: center;
    gap: 12px;
    font-size: 22px;
    line-height: 28px;
  }
  .card--back .brand__dot { width: 18px; height: 18px; }

  .website {
    position: absolute;
    left: 0;
    right: 0;
    top: 217px;
    text-align: center;
    font-size: 14.5px;
    letter-spacing: 0.1em;
  }
</style>
</head>
<body>
  <main class="stage">
    <section class="card card--front" aria-label="Business card front">
      <div class="brand">
        <span class="brand__dot"></span>
        <span class="brand__name">Miriam Delacourt Wellness</span>
      </div>
      <div class="contact">
        <p class="contact__name">Miriam Delacourt</p>
        <p class="contact__role">Yoga &amp; Coaching</p>
        <p class="contact__details">miriam@miriamdelacourt.com<br>(555) 014-2288</p>
      </div>
    </section>

    <section class="card card--back" aria-label="Business card back">
      <div class="brand">
        <span class="brand__dot"></span>
        <span class="brand__name">Miriam Delacourt Wellness</span>
      </div>
      <p class="website">www.miriamdelacourt.com</p>
    </section>
  </main>
</body>
</html>
```